Banner Ad and Digital Ad design for tradeshow

I need two graphics designed (can be same/similar design just different dimensions. We are an engineering firm practicing in the solid waste industry. We are a conference sponsor and need two graphics.
(1) Banner Ad - 300x250 - gif, png, jped, html, or other. Imagery with our mantra - Driven by purpose. Guided by stewardship. Striving for excellence.
(2) Digital Ad (static) - 1920x1080 hi-res jpg or png.

Target Market(s)

Solid Waste Management Industry (Environmental)

Industry/Entity Type

Environmental

Requirements
Must have
• Quality Aesthetic
Nice to have
• Great Imagery + our mantra

```html
<!DOCTYPE html>
<html lang="en">
<head>
<meta charset="utf-8">
<title>Coastal Resource Recovery Summit – Sponsor Ads</title>
<link rel="stylesheet" href="https://fonts.googleapis.com/css2?family=Archivo+Black&family=Poppins:wght@400;500&family=Roboto+Condensed:wght@600&display=swap">
<style>
  :root{
    --brown:#7a6543;
    --green:#6e8778;
    --photo-a:#d9d4cb;
    --photo-b:#8a9198;
    --white:#ffffff;
    --stage:#e6e7e9;
    --label:#8a8c90;
    --body:#6d6d6d;
  }
  *{margin:0;padding:0;box-sizing:border-box;}
  html,body{width:721px;height:1200px;overflow:hidden;background:var(--white);}
  body{position:relative;font-family:"Poppins",sans-serif;}

  .preview-zone{position:absolute;left:0;top:0;width:721px;height:448px;background:var(--white);}
  .screen-preview{position:absolute;left:193px;top:79px;width:582px;height:327px;transform:scale(0.5756);transform-origin:0 0;box-shadow:0 0 0 2px #222;}
  .stage{position:absolute;left:0;top:448px;width:721px;height:752px;background:var(--stage);}

  .format-label{position:absolute;left:0;width:721px;text-align:center;font-size:7.5px;color:var(--label);letter-spacing:.2px;}

  .ad{position:absolute;background:var(--white);overflow:hidden;}
  .ad.shadowed{box-shadow:2px 3px 5px rgba(0,0,0,.28);}

  .brand{position:absolute;display:flex;align-items:center;gap:5px;color:var(--green);font-family:"Poppins",sans-serif;font-weight:500;line-height:1;}
  .brand-square{background:var(--green);flex:none;}

  .headline{position:absolute;font-family:"Archivo Black",sans-serif;font-weight:400;color:var(--green);text-transform:uppercase;white-space:nowrap;}
  .headline .year{color:var(--brown);}

  .sponsor-tag{position:absolute;background:var(--brown);color:var(--white);font-family:"Roboto Condensed",sans-serif;font-weight:600;display:flex;align-items:center;justify-content:center;}

  .photo{position:absolute;background:linear-gradient(135deg,var(--photo-a) 0%,#b9b5ae 45%,var(--photo-b) 100%);}
  .accent-v,.accent-h{position:absolute;background:var(--green);}

  .copy{position:absolute;color:var(--body);}
  .copy p{margin-bottom:1em;}

  .learn-more{position:absolute;display:flex;border:.5px solid #bbb;background:var(--white);}
  .learn-more .label{display:flex;align-items:center;color:var(--white);text-transform:uppercase;font-weight:500;border-left:1.5px solid var(--white);white-space:nowrap;}
  .learn-more .icon{display:flex;align-items:center;justify-content:center;flex:1;}

  /* digital ad 582x327 */
  .digital .brand{left:453px;top:11px;font-size:11px;}
  .digital .brand-square{width:23px;height:23px;}
  .digital .brand small{display:block;font-size:7px;letter-spacing:2.2px;margin-top:2px;}
  .digital .headline{left:24px;top:26px;font-size:32px;line-height:39px;letter-spacing:-1px;}
  .digital .photo{left:40px;top:154px;width:179px;height:145px;border-top-right-radius:22px;}
  .digital .accent-v{left:0;top:195px;width:25px;height:132px;}
  .digital .accent-h{left:0;top:312px;width:107px;height:15px;}
  .digital .sponsor-tag{left:249px;top:157px;width:225px;height:25px;font-size:13px;border-top-right-radius:7px;}
  .digital .copy{left:249px;top:191px;width:310px;font-size:6.3px;line-height:7.6px;}
  .digital .learn-more{left:249px;top:280px;width:54px;height:12px;}
  .digital .learn-more .label{background:var(--green);font-size:4.2px;padding:0 5px;margin:1px;}

  /* banner ad 306x255 */
  .banner .brand{left:0;right:0;top:14px;justify-content:center;font-size:11px;}
  .banner .brand-square{width:21px;height:21px;}
  .banner .brand small{display:block;font-size:6.5px;letter-spacing:2.2px;margin-top:2px;}
  .banner .headline{left:0;width:306px;top:47px;text-align:center;font-size:17.5px;line-height:21px;letter-spacing:-.6px;}
  .banner .sponsor-tag{left:77px;top:94px;width:147px;height:17px;font-size:8.5px;border-top-right-radius:5px;}
  .banner .photo{left:22px;top:123px;width:124px;height:110px;border-top-right-radius:14px;}
  .banner .accent-v{left:0;top:154px;width:11px;height:101px;}
  .banner .accent-h{left:0;top:244px;width:82px;height:11px;}
  .banner .copy{left:163px;top:122px;width:126px;font-size:4.6px;line-height:5.6px;}
  .banner .learn-more{left:163px;top:225px;width:40px;height:9px;}
  .banner .learn-more .label{background:var(--brown);font-size:3.2px;padding:0 4px;margin:1px;}
</style>
</head>
<body>

<section class="preview-zone">
  <div class="ad digital screen-preview">
    <div class="brand"><span class="brand-square"></span><span>VERIDAN<small>ENGINEERING</small></span></div>
    <h1 class="headline"><span class="year">2026 Coastal</span><br>Resource Recovery<br>Summit</h1>
    <div class="accent-v"></div><div class="accent-h"></div>
    <div class="photo" role="img" aria-label="Photo of colleagues celebrating with a high five in a bright office"></div>
    <div class="sponsor-tag">Sponsor Name (Sponsor Level)</div>
    <div class="copy">
      <p>Lorem ipsum dolor sit amet, consectetuer adipiscing elit, sed diam nonummy nibh euismod tinciduntut laoreet dolore magna aliquam erat volutpat. Ut wisi enim ad minim veniam, quis nostrud exerci tation ullamcorper suscipit lobortis nisl ut</p>
      <p>Lorem ipsum dolor sit amet, cons ectetuer adipiscing elit, sed diam nonummy nibh euismod tincidunt ut laoreet dolore magna aliquam erat volutpat. Ut wisi enim ad minim veniam, quis nostrud exerci tation ullamcorper suscipit lobortis nisl ut aliquip ex ea commodo consequat.</p>
      <p>Lorem ipsum dolor sit amet, consectetuer adipiscing elit, sed diam nonummy nibh euismod tincidunt ut laoreet dolore magna aliquam erat volutpat. Ut wisi enim ad minim veniam, quis nostrud exerci.</p>
    </div>
    <a class="learn-more"><span class="label">Learn more</span><span class="icon"><svg width="10" height="7" viewBox="0 0 10 7"><path d="M1 1l3 2.5L1 6" fill="none" stroke="#555" stroke-width=".8"/><path d="M7 .5v6" stroke="#555" stroke-width=".8"/></svg></span></a>
  </div>
</section>

<section class="stage">
  <p class="format-label" style="top:41px;">Banner Ad - 300x250</p>

  <div class="ad banner shadowed" style="left:206px;top:59px;width:306px;height:255px;">
    <div class="brand"><span class="brand-square"></span><span>VERIDAN<small>ENGINEERING</small></span></div>
    <h2 class="headline">2026 Coastal Resource<br>Recovery Summit</h2>
    <div class="sponsor-tag">Sponsor Name (Sponsor Level)</div>
    <div class="accent-v"></div><div class="accent-h"></div>
    <div class="photo" role="img" aria-label="Photo of colleagues celebrating with a high five in a bright office"></div>
    <div class="copy">
      <p>Lorem ipsum dolor sit amet, consectetuer adipiscing elit, sed diam nonummy nibh euismod tincidunt ut laoreet dolore magna aliquam erat volutpat. Ut wisi enim ad minim veniam, quis nostrud exerci tation ullamcorper suscipit lobortis nisl ut</p>
      <p>Lorem ipsum dolor sit amet, cons ectetuer adipiscing elit, sed diam nonummy nibh euismod tincidunt ut laoreet dolore magna aliquam erat volutpat. Ut wisi enim ad minim veniam, quis nostrud exerci tation ullamcorper suscipit lobortis nisl ut aliquip ex ea commodo consequat.</p>
      <p>Lorem ipsum dolor sit amet, consectetuer adipiscing elit, sed diam nonummy nibh euismod tincidunt ut laoreet dolore magna aliquam erat volutpat. Ut wisi enim ad minim veniam, quis nostrud exerci.</p>
    </div>
    <a class="learn-more"><span class="label">Learn more</span><span class="icon"><svg width="8" height="6" viewBox="0 0 10 7"><path d="M1 1l3 2.5L1 6" fill="none" stroke="#555" stroke-width=".9"/><path d="M7 .5v6" stroke="#555" stroke-width=".9"/></svg></span></a>
  </div>

  <p class="format-label" style="top:347px;">Digital Ad (static) - 1920x1080</p>

  <div class="ad digital shadowed" style="left:68px;top:367px;width:582px;height:327px;">
    <div class="brand"><span class="brand-square"></span><span>VERIDAN<small>ENGINEERING</small></span></div>
    <h2 class="headline"><span class="year">2026 Coastal</span><br>Resource Recovery<br>Summit</h2>
    <div class="accent-v"></div><div class="accent-h"></div>
    <div class="photo" role="img" aria-label="Photo of colleagues celebrating with a high five in a bright office"></div>
    <div class="sponsor-tag">Sponsor Name (Sponsor Level)</div>
    <div class="copy">
      <p>Lorem ipsum dolor sit amet, consectetuer adipiscing elit, sed diam nonummy nibh euismod tinciduntut laoreet dolore magna aliquam erat volutpat. Ut wisi enim ad minim veniam, quis nostrud exerci tation ullamcorper suscipit lobortis nisl ut</p>
      <p>Lorem ipsum dolor sit amet, cons ectetuer adipiscing elit, sed diam nonummy nibh euismod tincidunt ut laoreet dolore magna aliquam erat volutpat. Ut wisi enim ad minim veniam, quis nostrud exerci tation ullamcorper suscipit lobortis nisl ut aliquip ex ea commodo consequat.</p>
      <p>Lorem ipsum dolor sit amet, consectetuer adipiscing elit, sed diam nonummy nibh euismod tincidunt ut laoreet dolore magna aliquam erat volutpat. Ut wisi enim ad minim veniam, quis nostrud exerci.</p>
    </div>
    <a class="learn-more"><span class="label">Learn more</span><span class="icon"><svg width="10" height="7" viewBox="0 0 10 7"><path d="M1 1l3 2.5L1 6" fill="none" stroke="#555" stroke-width=".8"/><path d="M7 .5v6" stroke="#555" stroke-width=".8"/></svg></span></a>
  </div>
</section>

</body>
</html>
```